Stationary Design needed for luxorious bespoke tailor

We need a design for our stationary items like businescards, letters, envelope and letter head / Signature for email. Our company "LE CORVAN" sells exclusively and luxourious bespoke garments and accessories for men. The desgins of letterhead, envelope and business card shoulderstand communicate luxury, high quality and good taste. We would like our logo to be used on the designs.

Target Market(s)

Gentleman with a high aproach and exclusive and luxourious suits and shirts, grooms, businesman,

Industry/Entity Type

It Company

Font styles to use
Sans Serif

Colors
ec1f27
ffffff

Requirements
Must have
• Logo, Companies name and adress, contactName internet & email, phone number line / mobile, VAT Nr. On Business Card frontpage only logo and name, adress companies on backpage. No VAT and Companies ID there. Company data; LE CORVAN AG Wiesenrain 42 4057 Basel Switzerland VAT: CHE 472 916 304 Tax Tel 41 61 594 17 36 Mobile 41 79 842 06 91 www.korvanmode.ch info@korvanmode.com.
Nice to have
• -Name And phone numbers need to be able to change (for different coworkers ...)
Should not have
• no VAT in Business Card

```html
<!DOCTYPE html>
<html lang="en">
<head>
<meta charset="utf-8">
<title>LE CORVAN – Stationery</title>
<link href="https://fonts.googleapis.com/css2?family=Montserrat:wght@400;500;600&display=swap" rel="stylesheet">
<style>
  :root{
    --red:#ec1f27;
    --paper:#f7f7f7;
    --ink:#2a2a2a;
    --charcoal:#2e2e2e;
    --charcoal-dark:#232323;
    --silver:#bdbdbd;
    --backdrop:#d6d6d8;
    --muted:#555;
  }
  *{box-sizing:border-box;margin:0;padding:0}
  html,body{width:1200px;height:991px;overflow:hidden}
  body{background:var(--backdrop);font-family:"Montserrat",sans-serif;color:var(--ink);position:relative}
  .piece{position:absolute;overflow:hidden}
  .brand{font-weight:500;letter-spacing:.06em;white-space:nowrap;line-height:1}

  /* Letterhead */
  .letterhead{left:70px;top:104px;width:398px;height:560px;background:var(--paper);border-top:4px solid var(--red);border-bottom:5px solid var(--charcoal)}
  .letterhead .brand{position:absolute;left:32px;top:34px;font-size:19px;color:var(--ink)}
  .letter-meta{position:absolute;left:32px;top:132px;font-size:5.6px;line-height:7.2px}
  .letter-meta .recipient{margin-top:8px}
  .letter-body{position:absolute;left:32px;top:206px;width:334px;font-size:5.4px;line-height:7.1px;text-align:justify}
  .letter-body .salutation{font-weight:600;margin-bottom:8px}
  .letter-body p{margin-bottom:7px}
  .signoff{position:absolute;left:32px;top:378px;font-size:5.6px;line-height:7.2px}
  .signoff strong{font-weight:600}
  .signature{position:absolute;left:84px;top:370px;width:82px;height:40px;background:linear-gradient(90deg,#e9ecf6,#dfe4f3);border-radius:3px}
  .letter-footer{position:absolute;left:32px;right:32px;bottom:14px;font-size:5px;line-height:7px;display:flex;justify-content:space-between;align-items:flex-end}
  .accent{color:var(--red)}

  /* Folder */
  .folder{left:506px;top:90px;width:432px;height:576px;background:var(--charcoal);border-radius:4px}
  .folder .spine{position:absolute;left:28px;top:0;bottom:0;width:1px;background:#1c1c1c}
  .folder .brand{position:absolute;left:0;right:0;top:100px;text-align:center;font-size:27px;color:var(--silver)}
  .folder .web{position:absolute;left:0;right:0;bottom:32px;text-align:center;font-size:7.5px;color:#9a9a9a;letter-spacing:.04em}

  /* Business cards */
  .card{left:66px;width:170px;height:94px}
  .card-front{top:696px;background:var(--paper);border-top:3px solid var(--red);border-bottom:3px solid var(--charcoal)}
  .card-front .brand{position:absolute;left:15px;top:22px;font-size:11px}
  .card-front .person{position:absolute;left:15px;top:66px;font-size:4.8px;line-height:6px}
  .card-front .person strong{font-weight:600;display:block}
  .card-back{top:810px;background:var(--charcoal)}
  .card-back .brand{position:absolute;left:0;right:0;top:33px;text-align:center;font-size:11px;color:var(--silver)}
  .card-back .contact{position:absolute;left:0;right:0;top:73px;text-align:center;font-size:3.8px;line-height:5px;color:#aaa}

  /* DL envelope front */
  .envelope-front{left:266px;top:696px;width:415px;height:208px;background:var(--paper);border-top:4px solid var(--red);border-bottom:4px solid var(--charcoal)}
  .envelope-front .brand{position:absolute;left:24px;top:30px;font-size:16px}
  .envelope-front .sender{position:absolute;left:32px;bottom:20px;font-size:5.2px;line-height:6.6px}
  .envelope-front .web{position:absolute;right:32px;bottom:20px;font-size:5.2px}

  /* DL envelope back */
  .envelope-back{left:718px;top:696px;width:415px;height:208px;background:var(--paper)}
  .envelope-back svg{position:absolute;left:0;top:0}
  .envelope-back .web{position:absolute;left:0;right:0;top:25px;text-align:center;font-size:5.2px;color:#9a9a9a}
</style>
</head>
<body>

<section class="piece letterhead" aria-label="Letterhead">
  <div class="brand">LE CORVAN</div>
  <div class="letter-meta">
    <div class="date">30.09.2015</div>
    <div class="recipient">Recipient's name<br>Lindenweg 8<br>10115 Berlin<br>Germany</div>
  </div>
  <div class="letter-body">
    <div class="salutation">Dear sir,</div>
    <p>Communication is a very integral part of living creatures, animals and humans. Communication may be verbal or written. Written communication however is only applicable to human beings. Can you even imagine a world without communication? Verbal communication can be through telephones, webcams or in person. Written communication is through letters, emails and mobile phone messages.</p>
    <p>In today's world of great inventions and technology, letters have somehow become redundant. It is the time for text messages or chats. But they still can communicate a lot more than all other modes of communication. Organizations and various government departments still bank on letters as a strong medium of communication. There is no comparison in costs of sending letters as compared to costs of mobile phone messages though – letters are far cheaper. Letters now commonly known as "hard copy documents" are considered more relevant and important than email copies of text messages as proof or evidence of some sort.</p>
    <p>Letters speak volumes about a person or an organization that writes it. So one must take utmost care ensuring that the language used in any letter is appropriate for the occasion for which it is being written. Since a letter is also a written proof or document, if there are certain things that should not form a part of it, then that too should be carefully handled.</p>
    <p>Writing a good letter is an art. But if for some reason someone is unable to write that perfect letter, these different types of letters provide a base for you to build on. Sample letters have been given for everyone to understand what all information needs to form a part of the letter type and then it can be customized.</p>
  </div>
  <div class="signoff">Yours Sincerely,<br><strong>Dario Velten</strong></div>
  <div class="signature" role="img" aria-label="Handwritten signature in blue ink"></div>
  <div class="letter-footer">
    <div>Wiesenrain 42, 4057 Basel, Switzerland · <span class="accent">Tel:</span> +41 61 594 17 36<br><span class="accent">Email:</span> info@korvanmode.ch · VAT: CHE-472.916.304 MwSt</div>
    <div>www.<span class="accent">korvanmode</span>.ch</div>
  </div>
</section>

<section class="piece folder" aria-label="Presentation folder">
  <div class="spine"></div>
  <div class="brand">LE CORVAN</div>
  <div class="web">www.<span class="accent">korvanmode</span>.ch</div>
</section>

<section class="piece card card-front" aria-label="Business card front">
  <div class="brand">LE CORVAN</div>
  <div class="person"><strong>LUKAS BRENNER</strong>Manager</div>
</section>

<section class="piece card card-back" aria-label="Business card back">
  <div class="brand">LE CORVAN</div>
  <div class="contact">Wiesenrain 42, 4057 Basel, Switzerland · <span class="accent">T</span> +41 61 594 17 36<br><span class="accent">M</span> +41 79 842 06 91 · <span class="accent">E</span> info@korvanmode.com · www.<span class="accent">korvanmode</span>.ch</div>
</section>

<section class="piece envelope-front" aria-label="Envelope front">
  <div class="brand">LE CORVAN</div>
  <div class="sender">Wiesenrain 42<br>4057 Basel, Switzerland</div>
  <div class="web">www.<span class="accent">korvanmode</span>.ch</div>
</section>

<section class="piece envelope-back" aria-label="Envelope back">
  <svg width="415" height="208" viewBox="0 0 415 208" aria-hidden="true">
    <path d="M0 0 H415 L398 58 Q396 63 390 63 H25 Q19 63 17 58 Z" fill="var(--charcoal)"/>
  </svg>
  <div class="web">www.<span class="accent">korvanmode</span>.ch</div>
</section>

</body>
</html>
```